Need a book cover design for a Lumora Book

Book has a long title and sub title so lots of words to fit on the cover.

I can be flexible a bit with the sub title due to the length of it but ideally i can get a design that takes everything.

Here is the title:

Tidal Geology: The Roots of Erosion, Sedimentation, and Canyon Forming

Sub Title/Heading
An Easy Primer on Coastal Cliffs, Dune Drift, River Beds, and Delta Mapping Methods

```html
<!DOCTYPE html>
<html lang="en">
<head>
<meta charset="utf-8">
<title>Tidal Geology – Lumora Book Cover</title>
<link rel="stylesheet" href="https://fonts.googleapis.com/css2?family=Oswald:wght@500;600;700&display=swap">
<style>
  :root {
    --ink-black: #000000;
    --title-red: #ff0000;
    --type-white: #ffffff;
    --glow-core: rgba(170, 225, 255, 0.5);
    --glow-mid: rgba(40, 130, 255, 0.32);
    --glow-edge: rgba(70, 60, 200, 0.18);
  }
  html, body {
    margin: 0;
    padding: 0;
    width: 800px;
    height: 1200px;
    overflow: hidden;
    background: var(--ink-black);
  }
  .cover {
    position: relative;
    width: 800px;
    height: 1200px;
    background: var(--ink-black);
    overflow: hidden;
    font-family: "Oswald", "Arial Narrow", sans-serif;
  }
  .cover-art {
    position: absolute;
    left: 0;
    top: 160px;
    width: 800px;
    height: 760px;
    background:
      radial-gradient(ellipse 46% 22% at 50% 55%, var(--glow-core), transparent 70%),
      radial-gradient(ellipse 50% 38% at 50% 55%, var(--glow-mid), transparent 75%),
      radial-gradient(ellipse 55% 48% at 48% 55%, var(--glow-edge), transparent 80%);
  }
  .cover-type {
    position: absolute;
    inset: 0;
    width: 800px;
    height: 1200px;
  }
  .tagline {
    fill: var(--type-white);
    font-family: "Oswald", "Arial Narrow", sans-serif;
    font-weight: 500;
    font-size: 27px;
  }
  .title-word {
    fill: var(--title-red);
    stroke: var(--type-white);
    stroke-width: 5px;
    stroke-linejoin: miter;
    paint-order: stroke;
    font-family: "Oswald", "Arial Narrow", sans-serif;
    font-weight: 600;
    font-size: 218px;
  }
  .subtitle-line {
    fill: var(--title-red);
    font-family: "Oswald", "Arial Narrow", sans-serif;
    font-weight: 700;
    font-size: 96px;
  }
  .author-name {
    fill: var(--type-white);
    font-family: "Oswald", "Arial Narrow", sans-serif;
    font-weight: 600;
    font-size: 54px;
  }
</style>
</head>
<body>
  <main class="cover">
    <div class="cover-art" role="img" aria-label="Glowing blue light trails looping around the centre of the cover"></div>

    <svg class="cover-type" viewBox="0 0 800 1200" xmlns="http://www.w3.org/2000/svg">
      <g class="tagline-block" text-anchor="middle">
        <text class="tagline" x="400" y="64" textLength="560" lengthAdjust="spacingAndGlyphs">An Easy Primer on Coastal Cliffs, Dune Drift,</text>
        <text class="tagline" x="400" y="102" textLength="560" lengthAdjust="spacingAndGlyphs">River Beds, and Delta Mapping Methods</text>
      </g>

      <g class="title-block" text-anchor="middle">
        <text class="title-word" x="400" y="309" textLength="540" lengthAdjust="spacingAndGlyphs">TIDAL</text>
        <text class="title-word" x="396" y="510" textLength="623" lengthAdjust="spacingAndGlyphs">GEOLOGY</text>
      </g>

      <g class="subtitle-block" text-anchor="middle">
        <text class="subtitle-line" x="400" y="773" textLength="520" lengthAdjust="spacingAndGlyphs">THE ROOTS OF</text>
        <text class="subtitle-line" x="400" y="871" textLength="400" lengthAdjust="spacingAndGlyphs">EROSION,</text>
        <text class="subtitle-line" x="400" y="969" textLength="560" lengthAdjust="spacingAndGlyphs">SEDIMENTATION,</text>
        <text class="subtitle-line" x="400" y="1066" textLength="604" lengthAdjust="spacingAndGlyphs">AND CANYON FORMING</text>
      </g>

      <text class="author-name" x="400" y="1161" text-anchor="middle" textLength="275" lengthAdjust="spacingAndGlyphs">Author Name</text>
    </svg>
  </main>
</body>
</html>
```